Weightloss company needs Business Card

We want a business card that is clean and professional, yet portrays that we are a friendly, innovative, and versatile program designed to fit the needs of our clients.
I would like there to be 2 sides, one side having an appointment card, and the other side containing the logo and business information. There can be decorations on both sides. The logo is attached.

Target Market(s)

Men and women 40-60

Industry/Entity Type

Business

Contact Information for Business Card

Font styles to use
Sans Serif

Requirements
Must have
• The logo, space for business information
Nice to have
• The colors in the logo
Should not have
• No pictures of people or food

```html
<!DOCTYPE html>
<html lang="en">
<head>
<meta charset="utf-8">
<title>Brightpath Wellness – Business Card</title>
<link href="https://fonts.googleapis.com/css2?family=Questrial&display=swap" rel="stylesheet">
<style>
  :root {
    --page-bg: #d9dadc;
    --card-white: #ffffff;
    --card-black: #050505;
    --brand-red: #e3223b;
    --brand-blue: #3fb8e6;
    --ink: #1a1a1a;
    --ink-light: #ffffff;
    --rule: #2a2a2a;
    --deco: #1c2a33;
  }
  * { box-sizing: border-box; margin: 0; padding: 0; }
  html, body { width: 1200px; height: 900px; overflow: hidden; }
  body {
    background: var(--page-bg);
    font-family: "Questrial", "Century Gothic", sans-serif;
    display: flex;
    flex-direction: column;
    align-items: center;
    justify-content: center;
    gap: 40px;
  }
  .card {
    position: relative;
    width: 620px;
    height: 354px;
    border-radius: 22px;
    overflow: hidden;
    box-shadow: 0 10px 28px rgba(0,0,0,0.25);
  }
  .brand {
    position: absolute;
    top: 40px;
    right: 40px;
    display: flex;
    align-items: center;
    gap: 12px;
    color: var(--brand-red);
    font-size: 30px;
    letter-spacing: 0.5px;
  }
  .brand-dot {
    width: 18px; height: 18px;
    border-radius: 50%;
    background: var(--brand-blue);
  }

  /* Appointment side */
  .card-appointment { background: var(--card-white); color: var(--ink); }
  .appointment-title {
    position: absolute;
    left: 48px; top: 168px;
    color: var(--brand-blue);
    font-size: 15px;
    letter-spacing: 0.5px;
  }
  .appointment-fields {
    position: absolute;
    left: 48px; right: 48px; top: 200px;
    list-style: none;
    display: flex; flex-direction: column; gap: 26px;
  }
  .appointment-fields li {
    display: flex; align-items: flex-end; gap: 10px;
    font-size: 17px;
  }
  .appointment-fields .fill-line {
    flex: 1;
    border-bottom: 1.2px solid var(--rule);
    height: 18px;
  }

  /* Contact side */
  .card-contact { background: var(--card-black); color: var(--ink-light); }
  .deco-ring {
    position: absolute;
    right: 40px; top: 150px;
    width: 130px; height: 130px;
    border-radius: 50%;
    border: 22px solid var(--deco);
  }
  .side-band {
    position: absolute;
    left: 0; bottom: 0;
    width: 20px; height: 170px;
    background: var(--brand-red);
  }
  .person {
    position: absolute;
    left: 56px; top: 160px;
  }
  .person-name {
    color: var(--brand-blue);
    font-size: 24px;
    letter-spacing: 0.5px;
  }
  .person-role { font-size: 14px; margin-top: 2px; letter-spacing: 0.5px; }
  .address { font-size: 15px; margin-top: 12px; line-height: 1.35; }
  .contact-list {
    list-style: none;
    margin-top: 12px;
    font-size: 15px;
    line-height: 1.4;
  }
  .contact-list li { display: flex; align-items: center; gap: 10px; }
  .contact-list svg { width: 13px; height: 13px; fill: none; stroke: var(--brand-blue); stroke-width: 2; }
</style>
</head>
<body>

<section class="card card-appointment" aria-label="Appointment side">
  <div class="brand"><span class="brand-dot"></span>Brightpath Wellness</div>
  <p class="appointment-title">APPOINTMENT</p>
  <ul class="appointment-fields">
    <li>Name:<span class="fill-line"></span></li>
    <li>Date:<span class="fill-line"></span></li>
    <li>Time:<span class="fill-line"></span></li>
  </ul>
</section>

<section class="card card-contact" aria-label="Contact side">
  <div class="brand"><span class="brand-dot"></span>Brightpath Wellness</div>
  <div class="deco-ring"></div>
  <div class="side-band"></div>
  <div class="person">
    <h1 class="person-name">MARCUS HALE</h1>
    <p class="person-role">DIRECTOR</p>
    <p class="address">Cedar Lane, 40218<br>Riverton, Northland</p>
    <ul class="contact-list">
      <li><svg viewBox="0 0 16 16"><path d="M3 2h3l1.5 3.5-2 1.2a8 8 0 0 0 3.8 3.8l1.2-2L14 10v3a1 1 0 0 1-1 1A11 11 0 0 1 2 3a1 1 0 0 1 1-1z"/></svg>+100 5550-1234</li>
      <li><svg viewBox="0 0 16 16"><rect x="1.5" y="3.5" width="13" height="9"/><path d="M1.5 3.5 8 9l6.5-5.5"/></svg>info@brightpathwellness.com</li>
      <li><svg viewBox="0 0 16 16"><circle cx="8" cy="8" r="6.5"/><path d="M1.5 8h13M8 1.5c3 3.5 3 9.5 0 13M8 1.5c-3 3.5-3 9.5 0 13"/></svg>www.brightpathwellness.com</li>
    </ul>
  </div>
</section>

</body>
</html>
```